Regenerative Medicine Brochure

I want a clean modern bi-fold or tri-fold brochure. We offer non-surgical joint repair for knees, shoulders, and hips. We have many services available including regenerative medicine including stem cell allograft, palatelet rich plasma, prolotherapy, triggerpoint injection, chiropractic and rehab therapies. We are a modern multidisciplinary clinic in coastal California. My logo is already complete and is a vibrant green color. I prefer lots of white space with some areas for service description and what conditions may benefit from the services. Design should convey modern treatments, upscale office and practice, and our target audience is older adults who want to maintain an active pain-free lifestyle.

Target Market(s)

Sports injuries, athletes, seniors who are active, knee pain, shoulder pain, arthritis.

Industry/Entity Type

Alternative Medicine

Font styles to use
Serif

Colors
9bcb3c

Requirements
Must have
• Small white space where we can write date, time, location of next event/class. Colors in brochure to coordinate with logo colors provided.

```html
<!DOCTYPE html>
<html lang="en">
<head>
<meta charset="utf-8">
<title>Brightwater Spine &amp; Joint – Brochure</title>
<link href="https://fonts.googleapis.com/css2?family=Nunito+Sans:ital,wght@0,300;0,400;0,600;0,700;1,700&display=swap" rel="stylesheet">
<style>
  :root{
    --green:#8cc63f;
    --green-deep:#74ad2a;
    --green-soft:#b9df73;
    --ink:#3a3a3a;
    --ink-soft:#5a5a5a;
    --paper:#ffffff;
    --stage:#ededed;
    --sky:#cfdbe3;
    --sea:#9fb4bf;
    --sand:#d8cbb8;
  }
  *{box-sizing:border-box;margin:0;padding:0}
  html,body{width:1200px;height:1000px;overflow:hidden}
  body{background:var(--stage);font-family:"Nunito Sans",Arial,sans-serif;color:var(--ink);position:relative}
  .sheet{position:absolute;background:var(--paper);overflow:hidden;box-shadow:0 2px 10px rgba(0,0,0,.12)}
  .outside{left:15px;top:215px;width:555px;height:470px}
  .inside{left:585px;top:215px;width:600px;height:480px}
  .abs{position:absolute}

  /* outside spread */
  .rule-top{position:absolute;top:17px;height:2px;background:var(--green)}
  .rule-bottom{position:absolute;bottom:10px;height:3px;background:var(--green)}
  .beach-photo{left:0;top:140px;width:555px;height:200px;background:linear-gradient(180deg,var(--sky) 0%,#dfe7ec 45%,var(--sea) 55%,#b9c6cc 68%,var(--sand) 78%,#cbbda8 100%)}
  .spine-band{left:230px;top:0;width:100px;height:470px;background:linear-gradient(90deg,rgba(140,198,63,.85),rgba(181,223,106,.7) 55%,rgba(140,198,63,.85))}
  .contact-title{left:25px;top:34px;font-size:12px;font-weight:700;color:var(--green)}
  .contact-list{left:25px;top:55px;list-style:none;font-size:7.5px;color:var(--ink)}
  .contact-list li{display:flex;align-items:center;gap:6px;height:16px}
  .dot-icon{width:9px;height:9px;flex:none}
  .address{left:25px;top:366px;display:flex;gap:6px;font-size:7.5px;line-height:10px}
  .hours{left:25px;top:392px;display:flex;gap:6px;font-size:7.5px;line-height:9.5px}
  .hours table{border-collapse:collapse}
  .hours td{padding-right:14px}
  .headline{right:18px;top:100px;text-align:right;font-size:13.5px;font-weight:700;font-style:italic;line-height:17px;color:#222}
  .headline em{color:var(--green)}
  .brand-out{right:20px;top:398px;font-size:23px;font-weight:300;color:#333;line-height:22px;text-align:left}

  /* inside spread */
  .about-box{left:5px;top:20px;width:290px;height:122px;background:var(--green)}
  .about-title{left:25px;top:24px;font-size:11px;font-weight:700;color:#fff}
  .about-copy{left:25px;top:40px;width:170px;font-size:5.6px;line-height:7.3px;color:#fff}
  .about-copy p+p{margin-top:4px}
  .portrait{left:198px;top:24px;width:78px;height:108px;background:linear-gradient(160deg,#6f8f4e,#9cb27a 50%,#5a7fb5)}
  .section-title{font-size:11px;font-weight:700;color:var(--green)}
  .service-grid{left:30px;top:166px;display:grid;grid-template-columns:repeat(4,58px);column-gap:6px;row-gap:4px}
  .service{font-size:5.8px;font-weight:700;font-style:italic;text-align:center;line-height:6.5px;height:61px}
  .service .thumb{height:44px;margin-bottom:2px}
  .body-copy{font-size:5.6px;line-height:7.3px;color:var(--ink-soft)}
  .body-copy p+p{margin-top:5px}
  .q{font-size:6.4px;font-weight:700;font-style:italic;color:#333;margin:7px 0 5px}
  .divider{left:296px;top:0;width:1px;height:480px;background:#e2e2e2}
  .icons{left:330px;top:30px;display:flex;gap:16px}
  .icon{width:30px;text-align:center;font-size:5.8px;font-weight:700;font-style:italic}
  .icon .shape{width:22px;height:22px;margin:0 auto 3px;background:var(--green);border-radius:4px}
  .foot-contact{left:330px;top:442px;list-style:none;font-size:5.6px;line-height:7px}
  .foot-contact li{display:flex;gap:4px;align-items:center}
  .foot-contact li::before{content:"";width:5px;height:5px;border-radius:50%;background:var(--green)}
  .brand-in{right:18px;top:449px;font-size:10px;font-weight:300;color:#333}
</style>
</head>
<body>

<!-- outside spread -->
<section class="sheet outside" aria-label="Brochure outside">
  <div class="rule-top" style="left:0;width:230px"></div>
  <div class="rule-top" style="left:330px;width:225px"></div>

  <h3 class="abs contact-title">Contact Us</h3>
  <ul class="abs contact-list">
    <li><svg class="dot-icon" viewBox="0 0 10 10"><circle cx="5" cy="5" r="5" fill="#8cc63f"/><path d="M3 2.6l1 .9-.5.8a3.5 3.5 0 0 0 2.2 2.2l.8-.5.9 1-.6.7C4.9 7.6 2.5 5.1 2.3 3.2z" fill="#fff"/></svg>805-555-0142</li>
    <li><svg class="dot-icon" viewBox="0 0 10 10"><circle cx="5" cy="5" r="5" fill="#8cc63f"/><path d="M3 2.6l1 .9-.5.8a3.5 3.5 0 0 0 2.2 2.2l.8-.5.9 1-.6.7C4.9 7.6 2.5 5.1 2.3 3.2z" fill="#fff"/></svg>805-555-0187</li>
    <li><svg class="dot-icon" viewBox="0 0 10 10"><circle cx="5" cy="5" r="5" fill="#8cc63f"/><rect x="2.5" y="3.3" width="5" height="3.4" fill="none" stroke="#fff" stroke-width=".8"/><path d="M2.5 3.3L5 5.2l2.5-1.9" fill="none" stroke="#fff" stroke-width=".8"/></svg>hello@brightwaterjoint.com</li>
    <li><svg class="dot-icon" viewBox="0 0 10 10"><circle cx="5" cy="5" r="5" fill="#8cc63f"/><rect x="2.4" y="2.8" width="5.2" height="4.4" rx=".5" fill="none" stroke="#fff" stroke-width=".8"/><line x1="2.4" y1="4.1" x2="7.6" y2="4.1" stroke="#fff" stroke-width=".7"/></svg>www.brightwaterjoint.com</li>
  </ul>

  <div class="abs beach-photo" role="img" aria-label="Photo of an older couple walking barefoot along the shore of a calm beach"></div>
  <div class="abs spine-band"></div>

  <h2 class="abs headline">Your Regenerative<br>Medicine <em>Specialists</em></h2>

  <div class="abs address">
    <svg class="dot-icon" viewBox="0 0 10 10"><circle cx="5" cy="5" r="5" fill="#8cc63f"/><path d="M5 2a1.9 1.9 0 0 1 1.9 1.9C6.9 5.3 5 7.8 5 7.8S3.1 5.3 3.1 3.9A1.9 1.9 0 0 1 5 2z" fill="#fff"/><circle cx="5" cy="3.9" r=".7" fill="#8cc63f"/></svg>
    <div>2480 Harbor Lane<br>Seaview, CA 93000</div>
  </div>
  <div class="abs hours">
    <svg class="dot-icon" viewBox="0 0 10 10"><circle cx="5" cy="5" r="5" fill="#8cc63f"/><path d="M2.8 5.1l1.5 1.5 3-3.2" fill="none" stroke="#fff" stroke-width="1"/></svg>
    <table>
      <tr><td>Monday</td><td>8:00 am - 6:00 pm</td></tr>
      <tr><td>Tuesday</td><td>8:00 am - 12:00 pm</td></tr>
      <tr><td>Wednesday</td><td>8:00 am - 6:00 pm</td></tr>
      <tr><td>Thursday</td><td>8:00 am - 12:00 pm</td></tr>
      <tr><td>Friday</td><td>8:00 am - 6:00 pm</td></tr>
      <tr><td>Saturday</td><td>Closed</td></tr>
      <tr><td>Sunday</td><td>Closed</td></tr>
    </table>
  </div>

  <div class="abs brand-out">Brightwater<br>spine &amp; joint</div>
  <div class="rule-bottom" style="left:0;width:230px"></div>
  <div class="rule-bottom" style="left:330px;width:225px"></div>
</section>

<!-- inside spread -->
<section class="sheet inside" aria-label="Brochure inside">
  <div class="rule-top" style="left:0;width:600px;top:6px"></div>
  <div class="abs divider"></div>

  <div class="abs about-box"></div>
  <h3 class="abs about-title">About Practice</h3>
  <div class="abs about-copy">
    <p>Daniel Harlow, DC, is an experienced chiropractor offering compassionate, dedicated care at Brightwater Spine &amp; Joint in Seaview, California. For more than 15 years, Dr. Harlow and his team have delivered gentle and effective chiropractic and wellness care for families on the central coast.</p>
    <p>Dr. Harlow focuses his practice on personalized care through chiropractic and is part of the integrated team of medical providers. He offers complete chiropractic family care — including prenatal care and pediatrics. Dr. Harlow has advanced training in auto accident care to provide safe and effective pain relief without the need for drugs or surgery.</p>
  </div>
  <div class="abs portrait" role="img" aria-label="Portrait photo of the chiropractor outdoors"></div>

  <h3 class="abs section-title" style="left:30px;top:148px">Services We Offer</h3>
  <div class="abs service-grid">
    <div class="service"><div class="thumb" role="img" aria-label="Cell illustration" style="background:linear-gradient(135deg,#3f8fc4,#9fd3ea)"></div>Regenerative Medicine</div>
    <div class="service"><div class="thumb" role="img" aria-label="Driver with neck pain" style="background:linear-gradient(135deg,#2e5f8a,#c9a98c)"></div>Auto Injury Treatment</div>
    <div class="service"><div class="thumb" role="img" aria-label="Chiropractic adjustment" style="background:linear-gradient(135deg,#dfe6e2,#8fb7b0)"></div>Chiropractic Care</div>
    <div class="service"><div class="thumb" role="img" aria-label="Person holding lower back" style="background:linear-gradient(135deg,#dcdde0,#8a98b0)"></div>Sciatica</div>
    <div class="service"><div class="thumb" role="img" aria-label="Tired person resting on sofa" style="background:linear-gradient(135deg,#c8c6c4,#8e8a88)"></div>Fibromyalgia</div>
    <div class="service"><div class="thumb" role="img" aria-label="Hands on a painful knee" style="background:linear-gradient(135deg,#6b5a52,#d3ae95)"></div>Arthritis</div>
    <div class="service"><div class="thumb" role="img" aria-label="Patient in rehabilitation session" style="background:linear-gradient(135deg,#d7dde0,#9aa9b3)"></div>Rehabilitation</div>
    <div class="service"><div class="thumb" role="img" aria-label="Person holding knee" style="background:linear-gradient(135deg,#b9b2ae,#7c89a6)"></div>Knee Pain</div>
  </div>

  <div class="abs body-copy" style="left:30px;top:298px;width:255px">
    <p>For joint arthritis and muscle pain and injuries, the team at Brightwater Spine &amp; Joint offers minimally invasive regenerative medicine techniques to help you recover from chronic pain. Located in Seaview, California, the medical team utilizes advanced restorative techniques to support the natural healing of injured joints and soft tissues without the need for surgery. To learn more, schedule a consultation online or by phone today.</p>
  </div>

  <h3 class="abs section-title" style="left:30px;top:345px">Regenerative Medicine Q &amp; A</h3>
  <div class="abs body-copy" style="left:30px;top:360px;width:255px">
    <div class="q">What is regenerative medicine?</div>
    <p>Regenerative medicine is a form of biotechnology that involves injecting regenerative medicine products into injured tissues to help your body repair damage. Regenerative medicine uses tissue engineering techniques to repair muscles, ligaments, cartilage, and tendons damaged by injuries, overuse, and osteoarthritis. The medical providers at Brightwater Spine &amp; Joint select from a variety of available treatments and products. These include amniotic allografts, hyaluronic acid, regenerative cells, and cytokines which are powerful growth factors that may help regenerate your own body's tissues.</p>
    <p>After you're injected with the amniotic allograft serum, the growth factors trigger repair at the site of injection. Over the course of the next several weeks, cells grow and multiply forming new tissue.</p>
  </div>
  <div class="rule-bottom" style="left:5px;width:290px"></div>

  <!-- right page -->
  <div class="abs body-copy" style="left:322px;top:14px;width:260px;color:#333">Regenerative medicine may be used in the following areas:</div>
  <div class="abs icons">
    <div class="icon"><div class="shape" role="img" aria-label="Shoulder icon"></div>Shoulder</div>
    <div class="icon"><div class="shape" role="img" aria-label="Elbow icon"></div>Elbow</div>
    <div class="icon"><div class="shape" role="img" aria-label="Wrist icon"></div>Wrist</div>
    <div class="icon"><div class="shape" role="img" aria-label="Hip icon"></div>Hip</div>
    <div class="icon"><div class="shape" role="img" aria-label="Knee icon"></div>Knee</div>
    <div class="icon"><div class="shape" role="img" aria-label="Ankle icon"></div>Ankle</div>
  </div>

  <div class="abs body-copy" style="left:322px;top:72px;width:262px">
    <p>There are many additional types of bone and soft tissue problems, including arthritis, that these injections may benefit.</p>
    <p>With regenerative medicine and amniotic allograft treatments, the team supports the natural healing abilities of your body without the need for drugs or surgical repair and painful recovery. However, not all forms of regenerative medicine are equal. At Brightwater Spine &amp; Joint, the team only works with the best regenerative medicine labs to ensure that the right kind of products are selected and that they are of the best quality and highest safety.</p>
    <div class="q">How does regenerative medicine work?</div>
    <p>The team uses lab-grade products that are sterilized and processed to inject into the injured area. Once injected, it is thought that these powerful products differentiate into a variety of tissues to trigger your own body to repair damaged tissues. This damage may involve minor tears in muscles, ligaments, and tendons, or cartilage and meniscus breakdown in joints.</p>
    <p>Regenerative medicine products contain the basic building blocks of the body tissues — including proteins, amino acids, and cytokines — responsible for healing and tissue growth. They also provide anti-inflammatory benefits by promoting repair of tissues affected by inflammation.</p>
    <p>While some inflammation is normal and has a benefit to healing injuries, long-term inflammation causes pain, swelling, and further damage to tissues. When you experience too much inflammation, it does more harm than good. Regenerative products may be able to correct the problem at the source and reduce the production of natural inflammatory chemicals so you can heal.</p>
    <div class="q">What can I expect from regenerative medicine treatments?</div>
    <p>During your visit, the team begins with a consultation and physical exam to determine if you're a candidate for regenerative medicine. They ask about your symptoms, condition, overall health, and lifestyle. If you're a candidate, the team then explains the procedure and what to expect both during and afterward.</p>
    <p>For the procedure, the team first cleans your skin and applies a topical numbing cream to your skin, if needed. Next, the team injects regenerative products into the treatment area. You may feel a slight pinch or burning sensation during the injection. The injection takes less than five minutes and you can return to your usual activities the same day. Mild soreness at the site is possible for two to three days.</p>
    <p>Over the coming weeks and months, the injected products help repair damaged tissues at the treatment site. Most people notice results after two months. Follow-up care may be recommended based on your condition and initial results. Speak to the team to see if regenerative medicine is right for you.</p>
    <p>To learn more, schedule a visit online or by phone at Brightwater Spine &amp; Joint now.</p>
  </div>

  <div class="abs" style="left:322px;top:437px;width:262px;height:1px;background:#ddd"></div>
  <ul class="abs foot-contact">
    <li>805-555-0142</li>
    <li>805-555-0187</li>
    <li>hello@brightwaterjoint.com</li>
    <li>www.brightwaterjoint.com</li>
  </ul>
  <div class="abs brand-in">Brightwater spine &amp; joint</div>
  <div class="rule-bottom" style="left:305px;width:290px"></div>
</section>

</body>
</html>
```